Specialized tax accounting firm needs letterhead design

We need a letterhead design for a professional services firm called R. Desmond Pell Inc. The firm is essentially a very specialized tax accounting firm - instead of serving the end consumer, we support other public accounting firms in the area of Canadian and U.S. tax advisory and compliance (i.e. they call us on tax issues too complex for the general practitioner. Our byline is "Tax Support Services for Public Accounting Firms". Our letterhead should utilize our logo and be based on colours present in our logo (see file attached). The final design needs to convey professionalism and trustworthiness (we're hired by accountants after all!) while being creative and eye-catching.

I've attached:
The font used in the logo
The logo itself in a variety of file formats
A single page showing the key firm information which should be appearing in the letterhead

Please note that there is much more leather background around the logo than needs to be incorporated in the letterhead.

Industry/Entity Type

Accounting

```html
<!DOCTYPE html>
<html lang="en">
<head>
<meta charset="utf-8">
<title>R. Desmond Pell Inc. — Letterhead</title>
<link href="https://fonts.googleapis.com/css2?family=Source+Sans+3:wght@400&display=swap" rel="stylesheet">
<style>
  :root {
    --backdrop: #e6e4e1;
    --paper: #ffffff;
    --paper-shade: #f1f1f1;
    --band: #0d0d0d;
    --band-edge: #1c1c1c;
    --orange: #f37c22;
    --amber: #f7b93a;
    --rule-blue: #2a8fc6;
    --ink-light: #ffffff;
    --ink-dark: #2b2b2b;
  }
  html, body {
    margin: 0;
    padding: 0;
    width: 942px;
    height: 1200px;
    overflow: hidden;
    background: var(--backdrop);
    font-family: "Source Sans 3", sans-serif;
    font-weight: 400;
  }
  .letterhead {
    position: absolute;
    left: 35px;
    top: 30px;
    width: 871px;
    height: 1130px;
    background: linear-gradient(135deg, var(--paper) 40%, var(--paper-shade) 100%);
    box-shadow: 0 2px 6px rgba(0,0,0,.25);
  }
  .side-strip {
    position: absolute;
    left: 0;
    top: 0;
    width: 57px;
    height: 100%;
    background: linear-gradient(90deg, var(--orange) 0%, var(--amber) 100%);
  }
  .side-rule {
    position: absolute;
    left: 57px;
    top: 0;
    width: 2px;
    height: 100%;
    background: var(--rule-blue);
  }
  .header-band {
    position: absolute;
    left: 59px;
    top: 0;
    right: 0;
    height: 92px;
    background: linear-gradient(180deg, var(--band-edge), var(--band));
  }
  .brand {
    position: absolute;
    left: 28px;
    top: 28px;
    display: flex;
    align-items: center;
    gap: 12px;
    color: var(--ink-light);
  }
  .brand-dot {
    width: 22px;
    height: 22px;
    border-radius: 50%;
    background: var(--orange);
    flex: none;
  }
  .brand-name {
    margin: 0;
    font-size: 27px;
    line-height: 34px;
    letter-spacing: .5px;
    white-space: nowrap;
  }
  .byline {
    position: absolute;
    left: 28px;
    top: 68px;
    margin: 0;
    font-size: 11px;
    letter-spacing: .4px;
    color: var(--ink-light);
    opacity: .8;
    white-space: nowrap;
  }
  .address {
    position: absolute;
    left: 643px;
    top: 16px;
    padding-left: 7px;
    border-left: 1px solid var(--ink-light);
    font-size: 13.5px;
    line-height: 20px;
    color: var(--ink-light);
    font-style: normal;
  }
  .contact-line {
    position: absolute;
    left: 70px;
    top: 1098px;
    display: flex;
    gap: 16px;
    font-size: 13.5px;
    color: var(--ink-dark);
  }
  .contact-item {
    display: flex;
    align-items: center;
    gap: 5px;
  }
  .contact-item svg {
    width: 13px;
    height: 13px;
    fill: none;
    stroke: var(--ink-dark);
    stroke-width: 1.6;
  }
</style>
</head>
<body>
  <main class="letterhead">
    <div class="side-strip"></div>
    <div class="side-rule"></div>

    <header class="header-band">
      <div class="brand">
        <div class="brand-dot"></div>
        <p class="brand-name">R. Desmond Pell Inc.</p>
      </div>
      <p class="byline">Tax Support Services for Public Accounting Firms</p>
      <address class="address">
        18-410 Harlow Crescent<br>
        Bedford, Nova Scotia<br>
        Canada B4A 2K7
      </address>
    </header>

    <footer class="contact-line">
      <span class="contact-item">
        <svg viewBox="0 0 16 16"><circle cx="8" cy="8" r="7"/><path d="M5.5 4.5c-.5 3 2 6.5 5 7l1-1.5-1.8-1-1 .7c-1-.6-1.7-1.4-2.2-2.4l.7-1-1-1.8z"/></svg>
        902.555.0147
      </span>
      <span class="contact-item">
        <svg viewBox="0 0 16 16"><path d="M2 11V8l2-4h8l2 4v3zM2 11v2M14 11v2M3 8h10"/><circle cx="4.5" cy="9.5" r=".6"/><circle cx="11.5" cy="9.5" r=".6"/></svg>
        902.555.0192
      </span>
      <span class="contact-item">
        <svg viewBox="0 0 16 16"><rect x="1.5" y="5" width="13" height="9"/><path d="M1.5 5l6.5 5 6.5-5M3 5l5-3.5L13 5"/></svg>
        owen@pelltax.services
      </span>
      <span class="contact-item">
        <svg viewBox="0 0 16 16"><circle cx="8" cy="8" r="6.5"/><ellipse cx="8" cy="8" rx="3" ry="6.5"/><path d="M1.5 8h13M2.5 5h11M2.5 11h11"/></svg>
        www.pelltax.services
      </span>
    </footer>
  </main>
</body>
</html>
```